OTV Web Design Project

I'm looking for a small, friendly,functional, information based website. If you go through the attachments, you would know the nature of the business.
Updates

Hi,

I have uploaded a picture of the CEO, Mr. Darvesh Kolhi NAMPQ member. Please feel free to use it whereever appropriate.

Thanks!

Hello, I have uploaded some references. I like the colours used on the bar and would w

Example of a we page . I like this layout for the inside pages.

I am changing the tabs on my website to:

Home
About us
Services
Contact us

The services tab will have three sub pages:

Immigration
Education
AccommodationAccommodation

Target Market(s)

Young international students willing to come to Canada to study, young international students willing to immigrate to Canada, parents of the students

Industry/Entity Type

Business

Requirements
Must have
• OTV HOME
ABOUT US
CONTACT
SERVICES
TAG LINE

The website should look n feel trendy, smart, current, factual, trustworthy etc....
Nice to have
• I am looking for a bold, attractive, eye catchy home page with less text! Something that makes a statement....
Should not have
• No Clip art, flash animation, no bells n whistles please

```html
<!DOCTYPE html>
<html lang="en">
<head>
<meta charset="utf-8">
<title>OTV – About Us</title>
<link href="https://fonts.googleapis.com/css2?family=Kanit:wght@700;800&family=Lato:wght@400;700&display=swap" rel="stylesheet">
<style>
  :root {
    --red: #ed1c24;
    --black: #000000;
    --ink: #1a1a1a;
    --white: #ffffff;
    --rule: #dcdcdc;
    --map-tint: #fde9e9;
    --placeholder-text: #9a9a9a;
  }
  * { margin: 0; padding: 0; box-sizing: border-box; }
  html, body { width: 1200px; height: 764px; overflow: hidden; background: var(--white); }
  .page { position: relative; width: 1200px; height: 764px; font-family: "Lato", sans-serif; color: var(--ink); }

  .map-backdrop {
    position: absolute; left: 190px; top: 40px; width: 930px; height: 650px;
    background: radial-gradient(ellipse at 50% 45%, var(--map-tint) 0%, rgba(253,233,233,0.6) 45%, rgba(255,255,255,0) 72%);
  }

  .brand { position: absolute; left: 97px; top: 80px; }
  .brand-name {
    display: flex; align-items: center; gap: 10px;
    font-family: "Kanit", sans-serif; font-weight: 800; font-size: 74px; line-height: 74px;
    color: var(--black); letter-spacing: -1px;
  }
  .brand-dot { width: 22px; height: 22px; background: var(--red); border-radius: 50%; }
  .brand-tagline { font-family: "Lato", sans-serif; font-weight: 400; font-size: 13px; color: var(--ink); margin-top: 4px; }

  .headline { position: absolute; left: 427px; top: 46px; font-family: "Kanit", sans-serif; font-weight: 800; line-height: 54px; }
  .headline-top { font-size: 60px; color: var(--black); }
  .headline-bottom { font-size: 60px; color: var(--red); margin-left: 233px; }

  .main-nav { position: absolute; left: 97px; top: 200px; list-style: none; }
  .main-nav li {
    width: 147px; height: 28px; margin-bottom: 3.5px; background: var(--black);
    font-family: "Kanit", sans-serif; font-weight: 700; font-size: 17px; color: var(--white);
    display: flex; align-items: center; padding-left: 2px;
  }
  .main-nav li.is-active { background: var(--red); }
  .main-nav svg { margin-right: 5px; }

  .divider { position: absolute; left: 301px; top: 195px; width: 1px; height: 453px; background: var(--rule); }

  .about { position: absolute; left: 349px; top: 196px; }
  .about-title { font-size: 40px; font-weight: 400; color: var(--red); letter-spacing: -0.5px; line-height: 44px; margin-bottom: 18px; }
  .about p { font-size: 15px; line-height: 21px; color: var(--ink); margin-bottom: 21px; }
  .about .lead { width: 750px; }
  .about .narrow { width: 555px; }
  .highlight { color: var(--red); }

  .portrait {
    position: absolute; left: 916px; top: 388px; width: 188px; height: 232px; background: var(--black);
    display: flex; align-items: center; justify-content: center; text-align: center;
    font-family: "Kanit", sans-serif; font-weight: 700; font-size: 21px; line-height: 26px; color: var(--placeholder-text);
  }

  .member-badge { position: absolute; left: 97px; top: 660px; display: flex; align-items: center; gap: 10px; }
  .member-shape { width: 78px; height: 78px; border-radius: 50%; background: #7ea6d8; }
  .member-name { font-family: "Lato", sans-serif; font-weight: 700; font-size: 26px; color: #5a6b88; }

  .copyright { position: absolute; left: 0; width: 1200px; top: 701px; text-align: center; font-size: 11px; color: var(--ink); }

  .social { position: absolute; left: 977px; top: 697px; display: flex; gap: 4px; }
  .social span { width: 27px; height: 27px; border-radius: 50%; background: var(--black); }
  .social span:first-child { background: var(--red); }
</style>
</head>
<body>
<div class="page">
  <div class="map-backdrop" role="img" aria-label="Faint map of Canada in the background"></div>

  <header class="brand">
    <div class="brand-name">OTV <span class="brand-dot"></span></div>
    <div class="brand-tagline">Guiding you forward.......</div>
  </header>

  <h1 class="headline">
    <div class="headline-top">DARE TO DREAM</div>
    <div class="headline-bottom">CANADIAN...</div>
  </h1>

  <ul class="main-nav">
    <li><svg width="14" height="14" viewBox="0 0 14 14"><path d="M0 5h7V1l7 6-7 6V9H0z" fill="#fff"/></svg>Home</li>
    <li class="is-active"><svg width="14" height="14" viewBox="0 0 14 14"><path d="M0 5h7V1l7 6-7 6V9H0z" fill="#fff"/></svg>About Us</li>
    <li><svg width="14" height="14" viewBox="0 0 14 14"><path d="M0 5h7V1l7 6-7 6V9H0z" fill="#fff"/></svg>Services</li>
    <li><svg width="14" height="14" viewBox="0 0 14 14"><path d="M0 5h7V1l7 6-7 6V9H0z" fill="#fff"/></svg>Contact Us</li>
    <li><svg width="14" height="14" viewBox="0 0 14 14"><path d="M0 5h7V1l7 6-7 6V9H0z" fill="#fff"/></svg>OTV Mission</li>
  </ul>

  <div class="divider"></div>

  <section class="about">
    <h2 class="about-title">ABOUT US</h2>
    <p class="lead">Darvesh Kolhi, CEO of Onward Talent Ventures, has vast knowledge in the field of Student Recruitment &amp; Higher Education. He is an MBA from Canada and is very well known in the India-Canada education corridor since 2004. He has served as India, Africa &amp; Middle East Head for Ridgeview College in the past, in addition to providing consultant services for various elite institutions including, Harbourline College, BC, Maplecrest College, Ottawa, Prairie Technical College, Manitoba, and Coastline College, BC.</p>
    <p class="narrow">Mr. Kolhi contributed significantly towards Ridgeview College's immense growth of international students from his region. During his tenure, the college witnessed over <span class="highlight">400% increase</span> in enrolment. This was the highest increase in numbers a medium-sized college in Canada had ever witnessed!</p>
    <p class="narrow">Mr. Kolhi is a seasoned and well-respected professional in the Higher Education sector. His key strengths include Student Recruitment, Counseling and Agent Network Development. Darvesh has been a mentor in Training, and Team Lead for successfully launching and establishing overseas education services for various Indian businesses focusing on education. New Service Launches, Market Penetration and Development have been areas of focus for him within the industry.</p>
  </section>

  <div class="portrait" role="img" aria-label="Portrait photo of Darvesh Kolhi">Image Of<br>Darvesh Kolhi<br>Comes Here</div>

  <footer>
    <div class="member-badge"><span class="member-shape"></span><span class="member-name">NAMPQ</span></div>
    <p class="copyright">© 2013 onwardtalentventures.com. All rights reserved.</p>
    <div class="social" aria-label="Social links"><span></span><span></span><span></span><span></span></div>
  </footer>
</div>
</body>
</html>
```